Brell Stone Company Business Cards

Front and Back Business Card - logo and text setup - cool design. I need workable photoshop or illustrator files so I can setup each employee card with design that is created
Updates

Hi everyone, thank you for the great entries. Please no more white and blue cards - there are so many already - black and silver only now please. thanks!

Target Market(s)

Construction Industry - Facility Managers

Industry/Entity Type

Construction

Contact Information for Business Card

I really like contemporary simplistic looks - clean neat....not opposed to seeing some black backrounds

Requirements
Must have
• Logo/website address with design on front only - www.brellstone-example.com (logo attached)
• Back:
• Name/Title/Company Address/Phone/email address
Nice to have
• Cool design
Should not have
• Nothing gimmicky like Fire or Water - since we are a Fire Protection company - it has all been done

```html
<!DOCTYPE html>
<html lang="en">
<head>
<meta charset="utf-8">
<title>Brell Stone Company – Business Cards</title>
<link rel="stylesheet" href="https://fonts.googleapis.com/css2?family=Open+Sans:wght@400;600;700;800&display=swap">
<style>
  :root {
    --backdrop: #2a2a2c;
    --card: #1d1d1f;
    --card-edge: #2b2b2e;
    --silver: #b9bbbe;
    --accent: #ee4b3a;
    --text: #e6e6e6;
    --brand-blue: #2f4f8f;
  }
  * { margin: 0; padding: 0; box-sizing: border-box; }
  html, body {
    width: 1200px; height: 874px; overflow: hidden;
    background: var(--backdrop);
    font-family: "Open Sans", Arial, sans-serif;
  }
  .sheet {
    width: 1200px; height: 874px;
    display: flex; flex-direction: column; align-items: center; justify-content: center;
    gap: 40px;
  }
  .card {
    position: relative;
    width: 620px; height: 354px;
    background: var(--card);
    border: 1px solid var(--card-edge);
    border-radius: 18px;
    box-shadow: 0 10px 30px rgba(0,0,0,0.45);
    overflow: hidden;
  }
  /* Front */
  .card-front { display: flex; align-items: center; justify-content: center; }
  .front-brand {
    font-weight: 800;
    font-size: 70px;
    letter-spacing: -1px;
    color: var(--silver);
    line-height: 1;
  }
  /* Back */
  .contact {
    position: absolute; left: 56px; top: 70px;
    color: var(--text);
  }
  .contact-name {
    color: var(--accent);
    font-weight: 600;
    font-size: 22px;
    letter-spacing: 0.5px;
    text-transform: uppercase;
  }
  .contact-title { font-size: 16px; margin-top: 2px; }
  .contact-address { font-size: 14px; line-height: 1.35; margin-top: 12px; }
  .contact-lines { list-style: none; font-size: 14px; line-height: 1.4; margin-top: 12px; }
  .contact-lines .label { color: var(--accent); font-weight: 700; }
  .contact-web {
    color: var(--accent); font-size: 15px; font-weight: 600; margin-top: 12px;
  }
  .back-brand {
    position: absolute; right: 48px; bottom: 56px;
    display: flex; align-items: center; gap: 10px;
    font-weight: 800; font-size: 34px; letter-spacing: -0.5px;
    color: var(--brand-blue);
  }
  .back-brand .mark {
    width: 14px; height: 14px; background: var(--accent);
  }
</style>
</head>
<body>
<main class="sheet">
  <section class="card card-front" aria-label="Card front">
    <div class="front-brand">Brell Stone</div>
  </section>

  <section class="card card-back" aria-label="Card back">
    <div class="contact">
      <div class="contact-name">Dana Whitlow</div>
      <div class="contact-title">CEO/Founder</div>
      <div class="contact-address">48 Quarry Lane<br>Millbrook, NY 10500</div>
      <ul class="contact-lines">
        <li><span class="label">P.</span> (555) 014-2870</li>
        <li><span class="label">F.</span> (555) 014-2871</li>
        <li><span class="label">E.</span> info@brellstone-example.com</li>
      </ul>
      <div class="contact-web">www.brellstone-example.com</div>
    </div>
    <div class="back-brand"><span class="mark"></span>Brell Stone</div>
  </section>
</main>
</body>
</html>
```